stationery
business cards, letterhead, and envelopes
Professional
Marisol Dunkerly
Mortgage Loan Originator / Owner
418 Kettering Avenue Ste 2270
Honolulu HI 96813
TideRiverCredit@quillmail.com
www.BrightCedarLending.com
Lowest Rates In Hawaii !!!!!

```html
<!DOCTYPE html>
<html lang="en">
<head>
<meta charset="utf-8">
<title>Bright Cedar Lending — Stationery</title>
<link rel="stylesheet" href="https://fonts.googleapis.com/css2?family=Lato:wght@400;700&display=swap">
<style>
:root{
  --board:#efe6d6;
  --paper:#ffffff;
  --blue:#2f3c9a;
  --blue-light:#6f7cc4;
  --grey:#8c8f96;
  --grey-dark:#5d6068;
  --ink:#3a3f55;
  --label:#6b6459;
  --wash:#f3efe6;
}
*{box-sizing:border-box;margin:0;padding:0}
html,body{width:1200px;height:446px;overflow:hidden}
body{background:var(--board);font-family:"Lato",sans-serif;color:var(--ink);position:relative}
.sheet{position:absolute;background:var(--paper);box-shadow:0 1px 4px rgba(0,0,0,.22);overflow:hidden}
.sheet svg.swoosh{position:absolute;inset:0;width:100%;height:100%}
.label{position:absolute;font-size:6px;letter-spacing:.4px;color:var(--label);text-transform:capitalize;white-space:nowrap}
.brand{position:absolute;display:flex;align-items:center;gap:3px;font-weight:700;color:var(--blue);white-space:nowrap}
.brand .dot{border-radius:50%;background:var(--blue)}
.tagline{position:absolute;color:var(--grey-dark);font-size:4px;letter-spacing:.3px;white-space:nowrap}
.watermark{position:absolute;border-radius:50%;background:var(--wash)}
.lines{position:absolute;font-size:4px;line-height:6px;color:var(--ink);white-space:nowrap}
</style>
</head>
<body>

<div class="label" style="left:19px;top:176px">Stationery concepts</div>

<!-- Business card front -->
<div class="sheet card-front" style="left:19px;top:148px;width:149px;height:86px">
  <svg class="swoosh" viewBox="0 0 149 86" preserveAspectRatio="none">
    <path d="M128 0H149V86H112Q142 45 128 0Z" fill="var(--blue)"/>
    <path d="M122 0H128Q142 45 112 86H106Q134 45 122 0Z" fill="var(--grey)"/>
  </svg>
  <div class="brand" style="left:8px;top:9px;font-size:6px"><span class="dot" style="width:6px;height:6px"></span>Bright Cedar Lending</div>
  <div class="tagline" style="left:8px;top:18px">Lowest Rates In Hawaii !!!!!</div>
  <div class="lines" style="left:8px;top:46px">
    <div style="font-weight:700;color:var(--blue)">Marisol Dunkerly</div>
    <div>Mortgage Loan Originator / Owner</div>
    <div>Ph 808 555 0142</div>
    <div>Fx 808 555 0199</div>
  </div>
</div>
<div class="label" style="left:19px;top:243px">Business card front</div>

<!-- Business card back -->
<div class="sheet card-back" style="left:19px;top:278px;width:149px;height:86px">
  <svg class="swoosh" viewBox="0 0 149 86" preserveAspectRatio="none">
    <path d="M60 86Q120 78 149 56V86Z" fill="var(--blue)"/>
    <path d="M40 86Q115 74 149 50V56Q120 78 60 86Z" fill="var(--grey)"/>
  </svg>
  <div class="brand" style="left:28px;top:30px;font-size:8px"><span class="dot" style="width:8px;height:8px"></span>Bright Cedar Lending</div>
  <div class="tagline" style="left:46px;top:43px">Lowest Rates In Hawaii !!!!!</div>
</div>
<div class="label" style="left:19px;top:372px">Business card back</div>

<!-- Letterhead option 1 -->
<div class="sheet letterhead" style="left:233px;top:17px;width:218px;height:343px">
  <svg class="swoosh" viewBox="0 0 218 343" preserveAspectRatio="none">
    <path d="M196 0H218V343H176Q214 180 196 0Z" fill="var(--blue)"/>
    <path d="M190 0H196Q214 180 176 343H168Q206 180 190 0Z" fill="var(--grey)"/>
    <path d="M0 336Q90 318 176 326L172 343H0Z" fill="var(--grey)"/>
    <path d="M0 340Q90 326 174 334L172 343H0Z" fill="var(--blue)"/>
  </svg>
  <div class="brand" style="left:58px;top:12px;font-size:9px"><span class="dot" style="width:9px;height:9px"></span>Bright Cedar Lending</div>
  <div class="tagline" style="left:82px;top:26px">Lowest Rates In Hawaii !!!!!</div>
  <div class="watermark" role="img" aria-label="Faint brand circle" style="left:64px;top:82px;width:80px;height:80px"></div>
  <div class="lines" style="left:12px;top:290px">
    <div>418 Kettering Avenue Ste 2270, Honolulu HI 96813</div>
    <div>TideRiverCredit@quillmail.com</div>
  </div>
</div>
<div class="label" style="left:300px;top:368px">Letterhead option 1</div>

<!-- Letterhead option 2 -->
<div class="sheet letterhead" style="left:473px;top:17px;width:223px;height:343px">
  <svg class="swoosh" viewBox="0 0 223 343" preserveAspectRatio="none">
    <path d="M0 310Q110 300 223 322V343H0Z" fill="var(--grey)"/>
    <path d="M0 318Q120 312 223 330V343H0Z" fill="var(--blue)"/>
  </svg>
  <div class="brand" style="left:60px;top:12px;font-size:9px"><span class="dot" style="width:9px;height:9px"></span>Bright Cedar Lending</div>
  <div class="tagline" style="left:84px;top:26px">Lowest Rates In Hawaii !!!!!</div>
  <div class="watermark" role="img" aria-label="Faint brand circle" style="left:70px;top:82px;width:80px;height:80px"></div>
  <div class="lines" style="left:20px;top:288px;font-size:3.6px">418 Kettering Avenue Ste 2270 · TideRiverCredit@quillmail.com · www.BrightCedarLending.com</div>
</div>
<div class="label" style="left:545px;top:368px">Letterhead option 2</div>

<!-- Envelope back, blue band -->
<div class="sheet envelope" style="left:787px;top:17px;width:403px;height:78px">
  <svg class="swoosh" viewBox="0 0 403 78" preserveAspectRatio="none">
    <path d="M300 0H403V78H350Q330 40 300 0Z" fill="var(--blue)"/>
    <path d="M290 0H300Q330 40 350 78H340Q320 40 290 0Z" fill="var(--grey)"/>
  </svg>
</div>

<!-- Envelope back, grey flap -->
<div class="sheet envelope" style="left:787px;top:96px;width:403px;height:84px">
  <svg class="swoosh" viewBox="0 0 403 84" preserveAspectRatio="none">
    <path d="M0 0H403L360 38Q350 46 330 46H73Q53 46 43 38Z" fill="var(--grey-dark)"/>
  </svg>
</div>

<!-- Envelope back, white flap with seal -->
<div class="sheet envelope" style="left:787px;top:156px;width:403px;height:96px">
  <svg class="swoosh" viewBox="0 0 403 96" preserveAspectRatio="none">
    <path d="M0 0L43 42Q53 50 73 50H330Q350 50 360 42L403 0" fill="none" stroke="#d6d6d6" stroke-width="1.2"/>
    <circle cx="201" cy="52" r="9" fill="var(--blue)"/>
  </svg>
</div>

<!-- Envelope front -->
<div class="sheet envelope" style="left:787px;top:269px;width:403px;height:91px">
  <svg class="swoosh" viewBox="0 0 403 91" preserveAspectRatio="none">
    <path d="M190 91Q330 80 403 40V91Z" fill="var(--blue)"/>
    <path d="M160 91Q320 74 403 32V40Q330 80 190 91Z" fill="var(--grey)"/>
  </svg>
  <div class="brand" style="left:10px;top:10px;font-size:9px"><span class="dot" style="width:9px;height:9px"></span>Bright Cedar Lending</div>
  <div class="tagline" style="left:24px;top:24px">418 Kettering Avenue Ste 2270, Honolulu HI 96813</div>
</div>
<div class="label" style="left:1130px;top:368px">Envelope option 1</div>

</body>
</html>
```